Award-winnning Estate Agent needs a premium version of their 'For Sale' board design

We need a premium option for our 'For Sale' board design. We have a standard board that is attached to this brief, but were are looking to have a premium design version that we will use when selling exclusive properties. Our company name is Harbour Lane Estates and the name for this is exclusive selection is: 'The Harbour Collection'. The design needs to work with our current brand, but have a distinctive PREMIUM feel to it. I have uploaded the barnd guidelines and also some of the exisisting logo variations. We do NOT need a new logo but feel free to play around with colours, fonts, sizes etc. for the sign.

Target Market(s)

Property buyers & house hunters

Industry/Entity Type

Real Estate - Residential Property

Font styles to use
Sans Serif

Requirements
Must have
• A premium fee, must be square design, must be easy to read when driving past the sign
Nice to have
• I'm open ot ideas

```html
<!DOCTYPE html>
<html lang="en">
<head>
<meta charset="utf-8">
<title>Harbour Lane Estates – The Harbour Collection For Sale Board</title>
<link rel="stylesheet" href="https://fonts.googleapis.com/css2?family=Arimo:wght@400;700&family=Inter:wght@300;500;700;800&display=swap">
<style>
  :root {
    --navy: #2d3a8f;
    --mid-blue: #1677bd;
    --phone-blue: #0a72b8;
    --white: #ffffff;
  }
  * { box-sizing: border-box; margin: 0; padding: 0; }
  html, body { width: 1200px; height: 1200px; overflow: hidden; background: var(--white); }
  .board {
    position: relative;
    width: 1200px;
    height: 1200px;
    background: var(--white);
    border: 6px solid var(--navy);
    font-family: "Inter", Arial, sans-serif;
    overflow: hidden;
  }
  .brand-mark {
    position: absolute;
    left: 540px;
    top: 110px;
    width: 120px;
    height: 120px;
    background: var(--mid-blue);
  }
  .brand-name {
    position: absolute;
    left: 0;
    top: 318px;
    width: 100%;
    text-align: center;
    font-weight: 800;
    font-size: 70px;
    letter-spacing: -1px;
    color: var(--navy);
  }
  .banner {
    position: absolute;
    color: var(--white);
    display: flex;
    align-items: center;
    transform: rotate(-1.7deg);
    white-space: nowrap;
  }
  .banner-title {
    left: 158px;
    top: 452px;
    width: 786px;
    height: 126px;
    background: var(--navy);
    justify-content: center;
    padding-left: 20px;
    font-weight: 500;
    font-size: 100px;
    letter-spacing: -2px;
  }
  .banner-subtitle {
    left: 601px;
    top: 576px;
    width: 438px;
    height: 102px;
    background: var(--mid-blue);
    justify-content: center;
    padding-left: 30px;
    font-weight: 300;
    font-size: 84px;
    letter-spacing: -2px;
  }
  .sale-line {
    position: absolute;
    left: 240px;
    top: 760px;
    display: flex;
    align-items: center;
    gap: 18px;
  }
  .sale-for {
    font-weight: 800;
    font-size: 96px;
    color: var(--navy);
    letter-spacing: 1px;
    margin-top: 16px;
  }
  .sale-badge {
    width: 386px;
    height: 134px;
    background: var(--navy);
    border-radius: 18px;
    color: var(--white);
    font-weight: 800;
    font-size: 124px;
    line-height: 134px;
    text-align: center;
    letter-spacing: 2px;
  }
  .phone-line {
    position: absolute;
    left: 87px;
    top: 894px;
    height: 150px;
    display: flex;
    align-items: center;
    gap: 14px;
  }
  .phone-icon { width: 134px; height: 134px; flex: none; }
  .phone-number {
    font-family: "Arimo", Arial, sans-serif;
    font-weight: 700;
    font-size: 150px;
    line-height: 1;
    color: var(--phone-blue);
    letter-spacing: -7px;
    white-space: nowrap;
  }
  .web-band {
    position: absolute;
    left: 0;
    bottom: 0;
    width: 100%;
    height: 96px;
    background: var(--navy);
    color: var(--white);
    font-weight: 500;
    font-size: 62px;
    letter-spacing: -1px;
    text-align: center;
    line-height: 96px;
  }
</style>
</head>
<body>
  <main class="board">
    <div class="brand-mark" aria-hidden="true"></div>
    <p class="brand-name">Harbour Lane Estates</p>

    <h1 class="banner banner-title">The Harbour</h1>
    <p class="banner banner-subtitle">Collection</p>

    <div class="sale-line">
      <span class="sale-for">FOR</span>
      <span class="sale-badge">SALE</span>
    </div>

    <div class="phone-line">
      <svg class="phone-icon" viewBox="0 0 134 134" aria-hidden="true">
        <circle cx="67" cy="67" r="61" fill="none" stroke="var(--phone-blue)" stroke-width="10"/>
        <path d="M44 36c6-4 11-3 13 2l6 15c1 4-2 6-4 9 5 10 12 16 22 21 3-2 5-5 9-4l15 8c4 3 3 9-1 13-5 4-14 4-22 2-22-7-38-24-44-45-2-9 1-17 6-21z" fill="var(--phone-blue)"/>
      </svg>
      <span class="phone-number">01632 960418</span>
    </div>

    <footer class="web-band">www.harbourlaneestates.co.uk</footer>
  </main>
</body>
</html>
```